Tidewell Works's Friendbook Cover Design

I am in need of a social media cover for my company's Friendbook account. Please leverage the green logos and color palette attached.

Tidewell Works offers 2 primary services:
1.) Business Automation Services
2.) AI (artificial intelligence integrations)

While a lot of what we do is highly technical, what we deliver is not. In a nutshell, we help our clients to connect their data regardless of what application that data is sitting in. Because we can connect that data, often times we can:

A.) offer more intelligent marketing and help our client increase their revenue.
B.) automate highly repetitive tasks using technology and drive down their costs thus saving them money
C.) help our clients use AI to better serve their customers

You can read a little bit about our company here: https://www.tidewellworks.example

Our tagline is: "Connect data to increase the flow of profitability."

Visually, we'd like your help to illustrate the "connecting" of these applications. Please let me know if you have any questions.

Target Market(s)

Business Owners or Marketing Managers

Industry/Entity Type

Marketing technologies.

Font styles to use
Sans Serif

Requirements
Must have
• Please make every effort to have the cover compatible with the color palette of the attached images.
Should not have
• Please do not use the standard clipart or stock libraries of AI = robot. If you do, please make them small. We help business glue their data from different sources to solve real work problems. Little robots are overused.

```html
<!DOCTYPE html>
<html lang="en">
<head>
<meta charset="utf-8">
<title>Tidewell Works – Page Cover</title>
<link href="https://fonts.googleapis.com/css2?family=Arimo:wght@400;700&family=Carlito:wght@400;700&display=swap" rel="stylesheet">
<style>
  :root {
    --page-bg: #e9ebee;
    --bar-blue: #4267b2;
    --bar-dark: #29487d;
    --panel: #ffffff;
    --line: #dddfe2;
    --text: #1d2129;
    --muted: #90949c;
    --link: #4b4f56;
    --cta: #42b72a;
    --navy: #0a3564;
    --ocean: #1572b6;
    --sky: #2a9ad8;
    --leaf: #8dc63f;
    --leaf-dark: #6aa32a;
    --brand-blue: #1b5fb0;
    --photo-dark: #0d2a4a;
    --photo-mid: #2f6f9f;
    --photo-light: #9cc3dc;
  }
  * { margin: 0; padding: 0; box-sizing: border-box; }
  html, body {
    width: 1200px; height: 822px; overflow: hidden;
    background: var(--page-bg);
    font-family: "Arimo", "Arial", sans-serif;
    color: var(--text);
  }
  .page { position: relative; width: 1200px; height: 822px; overflow: hidden; }
  .abs { position: absolute; }

  /* top bar */
  .topbar { left: 0; top: 0; width: 1200px; height: 41px; background: var(--bar-blue); border-bottom: 1px solid var(--bar-dark); }
  .search { left: 71px; top: 8px; width: 499px; height: 25px; background: #fff; border-radius: 3px; font-size: 14px; color: var(--muted); padding: 4px 8px; }
  .search-btn { left: 530px; top: 8px; width: 40px; height: 25px; background: #f6f7f9; border-radius: 0 3px 3px 0; }
  .top-avatar { left: 755px; top: 8px; width: 28px; height: 25px; background: #fff; border-radius: 2px; }
  .top-avatar::after { content: ""; position: absolute; left: 9px; top: 8px; width: 9px; height: 9px; border-radius: 50%; background: var(--leaf); }
  .top-name { left: 791px; top: 12px; font-size: 14px; color: #fff; font-weight: 700; }
  .top-divider { left: 875px; top: 12px; width: 1px; height: 18px; background: var(--bar-dark); }
  .top-home { left: 884px; top: 12px; font-size: 14px; color: #fff; font-weight: 700; }
  .top-badge { left: 924px; top: 11px; padding: 1px 4px; font-size: 12px; font-weight: 700; color: #fff; background: var(--bar-dark); border-radius: 3px; }
  .top-icons { left: 985px; top: 9px; }

  /* left sidebar */
  .profile { left: 37px; top: 57px; width: 201px; height: 203px; background: #fff; border: 1px solid var(--line); display: flex; align-items: center; justify-content: center; gap: 8px; }
  .profile-dot { width: 12px; height: 12px; border-radius: 50%; background: var(--leaf); flex: none; }
  .profile-name { font-family: "Carlito", "Calibri", sans-serif; font-weight: 700; font-size: 29px; color: var(--leaf-dark); white-space: nowrap; }
  .page-title { left: 37px; top: 272px; font-size: 29px; color: var(--text); }
  .page-handle { left: 37px; top: 305px; font-size: 19px; color: var(--muted); }
  .side-nav { left: 35px; top: 350px; width: 203px; list-style: none; }
  .side-nav li { height: 35px; line-height: 35px; padding-left: 12px; font-size: 16px; color: var(--link); border-left: 4px solid transparent; }
  .side-nav li.active { background: #d8dce3; border-left-color: var(--bar-blue); font-weight: 700; color: var(--text); }
  .create-btn { left: 45px; top: 543px; width: 110px; height: 29px; background: var(--cta); color: #fff; font-size: 13px; font-weight: 700; text-align: center; line-height: 29px; border-radius: 3px; }

  /* cover */
  .cover { left: 250px; top: 49px; width: 916px; height: 344px; overflow: hidden;
    background: linear-gradient(100deg, var(--navy) 0%, var(--ocean) 45%, var(--sky) 70%); }
  .cover-photo { left: 346px; top: 0; width: 570px; height: 344px;
    background:
      radial-gradient(ellipse 45% 40% at 50% 58%, var(--photo-light) 0%, transparent 100%),
      linear-gradient(120deg, var(--photo-mid) 0%, var(--photo-dark) 55%, var(--photo-mid) 100%);
    -webkit-mask-image: linear-gradient(90deg, transparent 0%, #000 20%);
            mask-image: linear-gradient(90deg, transparent 0%, #000 20%); }
  .cover-wave { left: 0; top: 0; width: 916px; height: 344px; }
  .tagline { left: 25px; top: 50px; font-family: "Carlito", "Calibri", sans-serif; font-weight: 700; font-size: 27px; line-height: 33px; }
  .tagline-main { display: block; color: #fff; }
  .tagline-accent { display: block; color: var(--leaf); }
  .services-card { left: 18px; top: 148px; width: 321px; height: 128px; background: #fff; border-radius: 8px; padding: 10px 16px; font-family: "Carlito", "Calibri", sans-serif; }
  .services-title { color: var(--leaf); font-weight: 700; font-size: 27px; text-align: center; line-height: 32px; margin-bottom: 8px; }
  .services-list { list-style: none; }
  .services-list li { color: var(--brand-blue); font-weight: 700; font-size: 17px; line-height: 34px; white-space: nowrap; }
  .brand-tag { left: 740px; top: 0; width: 176px; height: 53px; background: #fff; border-radius: 0 0 0 16px; display: flex; align-items: center; justify-content: center; gap: 8px; }
  .brand-dot { width: 11px; height: 11px; border-radius: 50%; background: var(--leaf); }
  .brand-name { font-family: "Carlito", "Calibri", sans-serif; font-weight: 700; font-size: 22px; color: var(--leaf-dark); white-space: nowrap; }

  /* action bar */
  .action-bar { left: 250px; top: 397px; width: 916px; height: 52px; background: #fff; border: 1px solid var(--line); }
  .btn { height: 30px; top: 407px; background: #f6f7f9; border: 1px solid #ced0d4; border-radius: 2px; font-size: 12px; font-weight: 700; color: var(--link); line-height: 28px; text-align: center; }

  /* panels */
  .panel { background: #fff; border: 1px solid var(--line); border-radius: 3px; }
  .composer { left: 250px; top: 466px; width: 558px; height: 118px; }
  .composer-head { left: 250px; top: 466px; width: 558px; height: 38px; background: #f6f7f9; border-bottom: 1px solid var(--line); }
  .composer-tab { top: 478px; font-size: 13px; font-weight: 700; color: var(--link); }
  .mini-logo { width: 49px; height: 48px; background: #f0f2f5; border: 1px solid var(--line); }
  .mini-logo::after { content: ""; position: absolute; left: 19px; top: 18px; width: 10px; height: 10px; border-radius: 50%; background: var(--leaf); }
  .composer-hint { left: 321px; top: 533px; font-size: 15px; color: var(--muted); }
  .photos { left: 250px; top: 600px; width: 558px; height: 240px; }
  .photos-title { left: 262px; top: 613px; font-size: 15px; font-weight: 700; }
  .photos-rule { left: 250px; top: 645px; width: 558px; height: 1px; background: var(--line); }
  .photos-empty { left: 250px; top: 646px; width: 558px; height: 176px; background: #f2f3f5; }
  .photos-label { left: 250px; top: 710px; width: 558px; text-align: center; font-size: 42px; color: #b8bbc1; letter-spacing: 1px; }

  .side-box { left: 822px; width: 344px; }
  .side-label { font-size: 15px; color: var(--link); }
  .about-text { left: 834px; top: 660px; width: 322px; font-size: 14px; line-height: 19px; color: var(--text); }
  .likes-title { left: 889px; top: 755px; font-size: 13px; font-weight: 700; color: var(--link); }
  .likes-sub { left: 889px; top: 775px; font-size: 13px; color: var(--muted); }
</style>
</head>
<body>
<main class="page">

  <header class="abs topbar"></header>
  <div class="abs search">Search Friendbook</div>
  <div class="abs search-btn">
    <svg width="40" height="25" viewBox="0 0 40 25" aria-hidden="true"><circle cx="18" cy="11" r="5" fill="none" stroke="#4b4f56" stroke-width="2"/><line x1="22" y1="15" x2="26" y2="19" stroke="#4b4f56" stroke-width="2"/></svg>
  </div>
  <div class="abs top-avatar"></div>
  <div class="abs top-name">page name</div>
  <div class="abs top-divider"></div>
  <div class="abs top-home">Home</div>
  <div class="abs top-badge">20+</div>
  <svg class="abs top-icons" width="180" height="24" viewBox="0 0 180 24" aria-hidden="true">
    <g fill="#1d3a73">
      <circle cx="10" cy="8" r="5"/><path d="M2 22c0-6 4-8 8-8s8 2 8 8z"/>
      <circle cx="20" cy="9" r="4"/>
      <path d="M40 4h16a3 3 0 0 1 3 3v8a3 3 0 0 1-3 3h-8l-5 4v-4h-3a3 3 0 0 1-3-3V7a3 3 0 0 1 3-3z"/>
      <circle cx="78" cy="12" r="9"/>
      <rect x="110" y="8" width="4" height="4"/><rect x="117" y="8" width="4" height="4"/><rect x="124" y="8" width="4" height="4"/>
      <circle cx="163" cy="12" r="9"/>
    </g>
    <path d="M159 10l4 4 4-4" fill="none" stroke="#4267b2" stroke-width="2"/>
  </svg>

  <!-- left sidebar -->
  <div class="abs profile">
    <span class="profile-dot"></span>
    <span class="profile-name">Tidewell Works</span>
  </div>
  <div class="abs page-title">page name</div>
  <div class="abs page-handle">@page-name</div>
  <ul class="abs side-nav">
    <li class="active">Home</li>
    <li>About</li>
    <li>Photos</li>
    <li>Likes</li>
    <li>Posts</li>
  </ul>
  <div class="abs create-btn">Create a Page</div>

  <!-- cover -->
  <section class="abs cover">
    <div class="abs cover-photo" role="img" aria-label="Photo of hands typing on a laptop overlaid with glowing connected data icons"></div>
    <svg class="abs cover-wave" viewBox="0 0 916 344" aria-hidden="true">
      <path d="M0 344 C 150 320 260 300 312 270 C 340 250 355 230 362 205 C 352 260 330 300 290 344 Z" fill="#ffffff" opacity="0.95"/>
      <path d="M0 344 C 150 328 270 310 336 268" fill="none" stroke="var(--sky)" stroke-width="2.5" opacity="0.7"/>
    </svg>
    <h1 class="abs tagline">
      <span class="tagline-main">Connect data to increase</span>
      <span class="tagline-accent">the flow of profitability</span>
    </h1>
    <div class="abs services-card">
      <h2 class="services-title">Primary services:</h2>
      <ul class="services-list">
        <li>Business Automation Services</li>
        <li>AI (artificial intelligence integrations)</li>
      </ul>
    </div>
    <div class="abs brand-tag">
      <span class="brand-dot"></span>
      <span class="brand-name">Tidewell Works</span>
    </div>
  </section>

  <!-- action bar -->
  <div class="abs action-bar"></div>
  <div class="abs btn" style="left:260px;width:72px;">Like</div>
  <div class="abs btn" style="left:338px;width:85px;">Follow</div>
  <div class="abs btn" style="left:429px;width:75px;">Share</div>
  <div class="abs btn" style="left:508px;width:90px;">··· More ▾</div>
  <div class="abs btn" style="left:1048px;width:105px;">Message</div>

  <!-- composer -->
  <div class="abs panel composer"></div>
  <div class="abs composer-head"></div>
  <div class="abs composer-tab" style="left:268px;">✎ Status</div>
  <div class="abs composer-tab" style="left:343px;">▣ Photo/Video</div>
  <div class="abs mini-logo" style="left:260px;top:519px;"></div>
  <div class="abs composer-hint">Write something on this Page...</div>

  <!-- photos -->
  <div class="abs panel photos"></div>
  <div class="abs photos-title">Photos</div>
  <div class="abs photos-rule"></div>
  <div class="abs photos-empty"></div>
  <div class="abs photos-label">Photo Preview</div>

  <!-- right column -->
  <div class="abs panel side-box" style="top:468px;height:49px;"></div>
  <div class="abs side-label" style="left:836px;top:483px;">App Page</div>
  <div class="abs panel side-box" style="top:533px;height:39px;"></div>
  <svg class="abs" style="left:834px;top:544px;" width="16" height="16" viewBox="0 0 16 16" aria-hidden="true"><circle cx="6.5" cy="6.5" r="4.5" fill="none" stroke="#90949c" stroke-width="2"/><line x1="10" y1="10" x2="14" y2="14" stroke="#90949c" stroke-width="2"/></svg>
  <div class="abs side-label" style="left:866px;top:544px;color:var(--muted);">Search for posts on this Page</div>
  <div class="abs panel side-box" style="top:586px;height:51px;"></div>
  <svg class="abs" style="left:834px;top:600px;" width="20" height="20" viewBox="0 0 20 20" aria-hidden="true"><circle cx="8" cy="6" r="4" fill="#90949c"/><path d="M1 18c0-5 3-7 7-7s7 2 7 7z" fill="#90949c"/><path d="M16 4v6M13 7h6" stroke="#90949c" stroke-width="2"/></svg>
  <div class="abs" style="left:866px;top:603px;font-size:13px;color:var(--link);">Invite friends to like this Page</div>
  <div class="abs panel side-box" style="top:651px;height:190px;"></div>
  <p class="abs about-text">Veggies es bonus vobis, proinde vos postulo essum magis kohlrabi welsh onion daikon amaranth tatsoi tomatillo melon azuki bean garlic.</p>
  <div class="abs mini-logo" style="left:834px;top:753px;width:45px;height:44px;"></div>
  <div class="abs likes-title">535 Likes</div>
  <div class="abs likes-sub">You and 3 other friends like this</div>

</main>
</body>
</html>
```